Fernbrook premium pontoon cleaning and maintenance needs a business card design

we need a business card for a new company based in Brisbane and gold coast that offers to clean peoples pontoons using high pressure washers. The company name will be Fernbrook, and will offer premium pontoon cleaning and maintenance.
colours that can be used maybe black, lime green, grey, blue.but up for anything. cheers

Target Market(s)

people who own pontoons

Industry/Entity Type

Business

Contact Information for Business Card

contact
Rob Casworth
Duncan Pryle
mobile 0461 728 392
email Fernbrook@mailvista.net

Requirements
Nice to have
• like the look of black business cards the best

```html
<!DOCTYPE html>
<html lang="en">
<head>
<meta charset="utf-8">
<title>Fernbrook Business Card</title>
<link rel="stylesheet" href="https://fonts.googleapis.com/css2?family=Open+Sans:wght@400;700&display=swap">
<style>
  :root {
    --backdrop: #3a3a3a;
    --card-black: #050505;
    --card-white: #ffffff;
    --ink: #111111;
    --ink-soft: #2b2b2b;
    --lime: #2fb34a;
    --divider: #444444;
  }
  * { margin: 0; padding: 0; box-sizing: border-box; }
  html, body {
    width: 1200px;
    height: 900px;
    overflow: hidden;
    background: var(--backdrop);
    font-family: "Open Sans", Arial, sans-serif;
  }
  .canvas {
    width: 1200px;
    height: 900px;
    display: flex;
    flex-direction: column;
    align-items: center;
    justify-content: center;
    gap: 40px;
  }
  .card {
    width: 700px;
    height: 400px;
    position: relative;
    box-shadow: 0 10px 30px rgba(0,0,0,0.45);
  }
  .card--front {
    background: var(--card-black);
    display: flex;
    align-items: center;
    justify-content: center;
  }
  .card--back {
    background: var(--card-white);
  }
  .wordmark {
    display: flex;
    align-items: center;
    gap: 16px;
  }
  .wordmark__name {
    font-weight: 700;
    text-transform: uppercase;
    letter-spacing: 0.08em;
    line-height: 1;
  }
  .wordmark__square {
    width: 14px;
    height: 14px;
    background: var(--lime);
  }
  .card--front .wordmark__name {
    color: var(--card-white);
    font-size: 58px;
  }
  .card--back .wordmark {
    position: absolute;
    left: 150px;
    top: 110px;
  }
  .card--back .wordmark__name {
    color: var(--ink);
    font-size: 50px;
  }
  .details {
    position: absolute;
    left: 150px;
    top: 210px;
    display: flex;
    align-items: stretch;
  }
  .contacts-people {
    text-align: right;
    padding-right: 16px;
    padding-top: 42px;
    font-weight: 700;
    font-size: 19px;
    line-height: 1.25;
    color: var(--ink);
    text-transform: uppercase;
  }
  .details__divider {
    width: 1.5px;
    background: var(--divider);
  }
  .contact-list {
    list-style: none;
    padding-left: 16px;
    font-size: 16px;
    line-height: 1.45;
    color: var(--ink-soft);
  }
  .contact-list li {
    display: flex;
    align-items: center;
    gap: 8px;
  }
  .contact-list svg {
    width: 12px;
    height: 12px;
    flex: none;
  }
</style>
</head>
<body>
<main class="canvas">
  <section class="card card--front" aria-label="Card front">
    <div class="wordmark">
      <span class="wordmark__name">Fernbrook</span>
      <span class="wordmark__square"></span>
    </div>
  </section>

  <section class="card card--back" aria-label="Card back">
    <div class="wordmark">
      <span class="wordmark__name">Fernbrook</span>
      <span class="wordmark__square"></span>
    </div>
    <div class="details">
      <div class="contacts-people">
        <p>Rob Casworth</p>
        <p>Duncan Pryle</p>
      </div>
      <div class="details__divider"></div>
      <ul class="contact-list">
        <li>
          <svg viewBox="0 0 12 12" aria-hidden="true"><rect x="3" y="0.8" width="6" height="10.4" rx="1.2" fill="none" stroke="var(--lime)" stroke-width="1.3"/><line x1="5" y1="9.3" x2="7" y2="9.3" stroke="var(--lime)" stroke-width="1"/></svg>
          <span>0461 728 392</span>
        </li>
        <li>
          <svg viewBox="0 0 12 12" aria-hidden="true"><rect x="0.8" y="2.3" width="10.4" height="7.4" fill="none" stroke="var(--lime)" stroke-width="1.3"/><polyline points="1,2.6 6,6.6 11,2.6" fill="none" stroke="var(--lime)" stroke-width="1.2"/></svg>
          <span>Fernbrook@mailvista.net</span>
        </li>
      </ul>
    </div>
  </section>
</main>
</body>
</html>
```